K & R Fabrications HVAC Mechanical Contractor Business Card

We need a business card for a HVAC/Plumbing Mechanical Contractor. Our website is http://www.krfabrications-demo.com. We would like to include the picture of the person on the card. Pictures of people for mock-ups can be found on our website. The blue on our logo is our primary color. We'd like this to be bold yet professional without too many colors but with some color to make sure it stands out.

Industry/Entity Type

Business

Contact Information for Business Card

Font styles to use
Sans Serif

Colors
000000

Requirements
Must have
• Our logo
• Person's picture
• Company Name
• Company Phone
• Person's email address
• Person's phone number
Nice to have
• Company Address
Should not have
• Clip art

```html
<!DOCTYPE html>
<html lang="en">
<head>
<meta charset="utf-8">
<title>K &amp; R Fabrications – Business Card</title>
<link rel="stylesheet" href="https://fonts.googleapis.com/css2?family=Montserrat:wght@400;600;700&family=Source+Sans+3:wght@400;500;600&display=swap">
<style>
  :root {
    --brand-blue: #2f6fc4;
    --ink: #111111;
    --paper: #ffffff;
    --backdrop: #2b2d30;
    --photo-dark: #3b4045;
    --photo-light: #6a7075;
  }
  * { box-sizing: border-box; margin: 0; padding: 0; }
  html, body { width: 1200px; height: 790px; overflow: hidden; }
  body { background: var(--backdrop); position: relative; font-family: "Source Sans 3", Arial, sans-serif; }

  .card {
    position: absolute; left: 75px; top: 155px;
    width: 1050px; height: 480px;
    background: var(--paper);
    overflow: hidden;
  }

  .brand-mark {
    position: absolute; left: 80px; top: 35px;
    width: 280px; height: 120px;
    display: flex; align-items: center; gap: 18px;
  }
  .brand-mark__square { width: 70px; height: 70px; background: var(--brand-blue); flex: none; }
  .brand-mark__name {
    font-family: "Montserrat", Arial, sans-serif; font-weight: 700;
    font-size: 52px; color: var(--ink); letter-spacing: 1px; white-space: nowrap;
  }

  .company { position: absolute; left: 395px; top: 70px; }
  .company__name {
    font-family: "Montserrat", Arial, sans-serif; font-weight: 700;
    font-size: 26px; color: var(--ink); letter-spacing: 0.5px;
  }
  .company__trade {
    font-family: "Montserrat", Arial, sans-serif; font-weight: 400;
    font-size: 25px; color: var(--brand-blue); letter-spacing: 1.5px; margin-top: 2px;
  }

  .portrait {
    position: absolute; left: 678px; top: 200px;
    width: 315px; height: 222px;
    border: 4px solid var(--brand-blue);
    background: radial-gradient(ellipse at 40% 40%, var(--photo-light), var(--photo-dark));
  }

  .person { position: absolute; left: 70px; top: 240px; }
  .person__name {
    font-family: "Montserrat", Arial, sans-serif; font-weight: 700;
    font-size: 35px; color: var(--brand-blue); line-height: 1.1;
  }
  .person__title { font-size: 23px; color: var(--ink); font-weight: 500; }

  .address { position: absolute; left: 68px; top: 310px; font-size: 22px; color: var(--ink); font-weight: 500; }

  .contacts { position: absolute; top: 345px; font-size: 22px; color: var(--ink); font-weight: 500; list-style: none; }
  .contacts--phones { left: 66px; }
  .contacts--web { left: 280px; }
  .contacts li { display: flex; align-items: center; gap: 8px; height: 29px; }
  .contacts svg { width: 18px; height: 18px; fill: var(--brand-blue); flex: none; }

  .footer-band {
    position: absolute; left: 0; bottom: 0; width: 100%; height: 38px;
    background: var(--brand-blue);
  }
  .footer-band__tag {
    position: absolute; left: 640px; top: 3px; height: 32px; padding: 0 10px;
    background: var(--paper); display: flex; align-items: center;
    font-family: "Montserrat", Arial, sans-serif; font-weight: 700; font-size: 18px; color: var(--ink);
  }
</style>
</head>
<body>
  <section class="card">
    <div class="brand-mark">
      <span class="brand-mark__square"></span>
      <span class="brand-mark__name">K &amp; R</span>
    </div>

    <div class="company">
      <h1 class="company__name">K &amp; R FABRICATIONS, INC.</h1>
      <p class="company__trade">Mechanical Contractor</p>
    </div>

    <div class="portrait" role="img" aria-label="Portrait photo of Dan Mercer"></div>

    <div class="person">
      <h2 class="person__name">Dan Mercer</h2>
      <p class="person__title">Head of IT Services</p>
    </div>

    <p class="address">1450 Harbor Lane Fairview, WI 53999-0140</p>

    <ul class="contacts contacts--phones">
      <li><svg viewBox="0 0 24 24"><path d="M6 2c1 0 2 3 3 5 0 1-2 2-2 3 1 3 4 6 7 7 1 0 2-2 3-2 2 1 5 2 5 3 0 2-2 4-4 4C10 22 2 14 2 6c0-2 2-4 4-4z"/></svg>555-010-4421</li>
      <li><svg viewBox="0 0 24 24"><path d="M2 8c2-4 18-4 20 0l-1 3-4-1V8H7v2l-4 1zM6 12h12l3 9H3z"/></svg>555-010-7700</li>
      <li><svg viewBox="0 0 24 24"><path d="M6 3h12v5H6zM2 9h20v10h-3v-4H5v4H2zM6 16h12v6H6z"/></svg>555-010-7701</li>
    </ul>

    <ul class="contacts contacts--web">
      <li><svg viewBox="0 0 24 24"><path d="M2 5h20v14H2zM3 6l9 7 9-7"/></svg>dmercer@krfabrications-demo.com</li>
      <li><svg viewBox="0 0 24 24"><circle cx="12" cy="12" r="10"/><path d="M2 12h20M12 2v20M5 6h14M5 18h14" stroke="#fff" stroke-width="1.5" fill="none"/></svg>www.krfabrications-demo.com</li>
    </ul>

    <div class="footer-band">
      <span class="footer-band__tag">K &amp; R</span>
    </div>
  </section>
</body>
</html>
```